Floorplan brochure design for rental company

We need a brochure designed for our rental company, Bramble Tor Commons.
We have two different categories that we need on this brochure: townhomes (primary) and mobile homes. Size and layout is up to you... choose what you think works best for the information being presented. However, please do not use an odd shape or size; do use a size and format that can be printed by qelvaprint.com.
Font and color choices are up to you. If needed, the fonts from the logo are Americana Extra Bold and BlackJack.
Industry/Entity Type
It Company
Requirements
Must have
- 1. logo and office address/contact information
2. floorplans and prices from attached documents
3. amenities from attached document
Should not have
- Please do not use our website, brambletor.com, as a basis for any design or color scheme decisions. We are working on a redesign of that website with our new logo (attached).

```html
<!DOCTYPE html>
<html lang="en">
<head>
<meta charset="utf-8">
<title>Bramble Tor Commons — Brochure Cover</title>
<link rel="stylesheet" href="https://fonts.googleapis.com/css2?family=Open+Sans:wght@300;400;700&display=swap">
<style>
  :root {
    --backdrop: #808080;
    --paper: #ffffff;
    --door-green: #4f9a4f;
    --door-light: #6aae68;
    --door-edge: #3f8a40;
    --brand-green: #3d9a3a;
    --ink: #4a4a4a;
    --fold: #a8a8a8;
  }
  * { margin: 0; padding: 0; box-sizing: border-box; }
  html, body { width: 1200px; height: 900px; overflow: hidden; }
  body { background: var(--backdrop); font-family: "Open Sans", Arial, sans-serif; position: relative; }

  .brochure {
    position: absolute; left: 317px; top: 50px;
    width: 565px; height: 800px;
    background: var(--paper); overflow: hidden;
  }
  .door-photo { position: absolute; inset: 0; width: 565px; height: 800px; }

  .fold-line {
    position: absolute; left: 0; right: 0; top: 400px;
    border-top: 1px dashed var(--fold);
  }

  .panel { position: absolute; left: 0; width: 565px; height: 400px; }
  .panel--back { top: 0; transform: rotate(180deg); }
  .panel--front { top: 400px; }

  .headline {
    position: absolute; color: var(--ink);
    font-weight: 300; font-size: 22px; line-height: 31px; letter-spacing: 1px;
    text-transform: uppercase;
  }
  .panel--front .headline { right: 36px; top: 40px; text-align: right; }
  .panel--back .headline { left: 36px; top: 310px; font-size: 20px; line-height: 28px; }

  .wordmark {
    position: absolute; color: var(--brand-green);
    font-weight: 700; text-align: center; line-height: 1.15;
  }
  .wordmark .dot {
    display: block; margin: 0 auto 6px; border-radius: 50%;
    background: var(--brand-green);
  }
  .panel--front .wordmark { left: 398px; top: 168px; width: 130px; font-size: 15px; }
  .panel--front .wordmark .dot { width: 34px; height: 34px; }
  .panel--back .wordmark { left: 72px; top: 42px; width: 90px; font-size: 10px; }
  .panel--back .wordmark .dot { width: 20px; height: 20px; margin-bottom: 4px; }

  .phone-large {
    position: absolute; right: 29px; top: 333px;
    color: var(--brand-green); font-weight: 700; font-size: 26px; letter-spacing: 0.3px;
  }

  .contact { position: absolute; left: 36px; top: 132px; color: var(--ink); font-size: 12px; line-height: 20px; }
  .contact .company { font-weight: 700; font-size: 13px; letter-spacing: 0.5px; text-transform: uppercase; }
  .contact .phone { color: var(--brand-green); font-weight: 700; font-size: 13px; margin-bottom: 4px; }
  .contact .web { margin-top: 18px; }
</style>
</head>
<body>
  <main class="brochure">
    <svg class="door-photo" viewBox="0 0 565 800" role="img" aria-label="Photograph of a green six-panel front door slightly ajar with a silver knob">
      <defs>
        <linearGradient id="doorShade" x1="0" y1="0" x2="1" y2="1">
          <stop offset="0" stop-color="var(--door-green)"/>
          <stop offset="0.6" stop-color="var(--door-light)"/>
          <stop offset="1" stop-color="var(--door-green)"/>
        </linearGradient>
      </defs>
      <polygon points="0,0 273,0 351,800 0,800" fill="url(#doorShade)"/>
      <polygon points="252,0 273,0 351,800 332,800" fill="var(--door-edge)"/>
    </svg>

    <div class="fold-line"></div>

    <section class="panel panel--back">
      <div class="wordmark"><span class="dot"></span>Bramble Tor Commons</div>
      <div class="contact">
        <p class="company">Bramble Tor Commons</p>
        <p class="phone">281.555.0148</p>
        <p>48 Larkspur Lane</p>
        <p>Halvern, Texas 77612</p>
        <p class="web">www.brambletor.com</p>
      </div>
      <h2 class="headline">[c] Your<br>Community</h2>
    </section>

    <section class="panel panel--front">
      <h1 class="headline">[a] Step into<br>the good life</h1>
      <div class="wordmark"><span class="dot"></span>Bramble Tor Commons</div>
      <p class="phone-large">281.555.0148</p>
    </section>
  </main>
</body>
</html>
```